Financial Advisor needs a BOLD Business Card

I need a business card that is professional, and is also eye-catching and memorable. I would like to include my photo (several different professional photos have been uploaded). Preferred primary color is blue, or green, or dark purple. The final design should have a modern/contemporary look while communicating a professional image.

Target Market(s)

Individual Investors and Small Business Owners

Industry/Entity Type

Business

Contact Information for Business Card

[side 1:] Dale Korvanek Financial Advisor 58271 Marbleton Creek Rd., #340 St. Louis, MO 63907 (314) 555-0182 main (314) 555-0927 cell (314) 555-0346 fax daleK@qrvlx.com [side 2:] Life Insurance | Retirement | Employee Benefits

Font styles to use
Serif
Sans Serif

Requirements
Must have
• [disclaimer, text can be 7-9 point:] Securities offered through the B.W. Harbor Trading Company. Member NARCU/TLOB. Four Quarry Plaza, Cincinnati, Ohio 45917. 513-555-0263. Investment Advisory Services offered through B.W. Holdings Management Company.
Nice to have
• Bright, Light & Airy feel on Side 1 with contact data, bold patterns, high color contrast, modern or 3D look
Should not have
• Any symbols referring to money (e.g. $)

```html
<!DOCTYPE html>
<html lang="en">
<head>
<meta charset="utf-8">
<title>Dale Korvanek – Business Card</title>
<link href="https://fonts.googleapis.com/css2?family=Open+Sans:wght@400;600;700&display=swap" rel="stylesheet">
<style>
  :root {
    --page-bg: #e4e4e4;
    --card-dark: #26282b;
    --card-light: #ffffff;
    --brand-blue: #3d82d4;
    --disclaimer-blue: #1f5fae;
    --brand-green: #3a9a43;
    --label-green: #47b04f;
    --photo-top: #2f4a32;
    --photo-bottom: #1c2536;
  }
  * { margin: 0; padding: 0; box-sizing: border-box; }
  html, body {
    width: 1200px; height: 720px; overflow: hidden;
    background: var(--page-bg);
    font-family: "Open Sans", Arial, sans-serif;
  }
  .card {
    position: absolute;
    top: 241px;
    width: 420px; height: 240px;
    border-radius: 8px;
    overflow: hidden;
  }
  .card--front { left: 147px; background: var(--card-dark); }
  .card--back { left: 633px; background: var(--card-light); }

  .portrait {
    position: absolute;
    left: 22px; top: 21px;
    width: 135px; height: 198px;
    border-radius: 10px;
    background: linear-gradient(170deg, var(--photo-top) 0%, #3b4a50 40%, var(--photo-bottom) 100%);
    box-shadow: 0 0 8px rgba(220, 210, 150, 0.45);
  }

  .contact {
    position: absolute;
    left: 170px; top: 158px;
    width: 240px;
    color: var(--brand-blue);
    white-space: nowrap;
  }
  .contact__name {
    font-size: 10.5px; font-weight: 700;
    line-height: 15px;
    letter-spacing: 0.1px;
  }
  .contact__rule {
    width: 229px; height: 2px;
    background: var(--brand-green);
    margin-top: 1px;
  }
  .contact__line {
    font-size: 8.3px; font-weight: 400;
    line-height: 16px;
  }
  .contact__line:first-of-type { margin-top: 0; }
  .label { color: var(--label-green); }

  .services-tab {
    position: absolute;
    left: 142px; top: 0;
    width: 136px; height: 140px;
    background: var(--brand-green);
    border-radius: 0 0 8px 8px;
    display: flex; flex-direction: column; justify-content: flex-end;
    padding-bottom: 30px;
    text-align: center;
    color: #ffffff;
    font-size: 9.6px; font-weight: 600;
    line-height: 16px;
  }

  .disclaimer {
    position: absolute;
    left: 0; right: 0; top: 142px;
    text-align: center;
    color: var(--disclaimer-blue);
    font-size: 8.3px; font-weight: 600;
    line-height: 16px;
  }
</style>
</head>
<body>
  <section class="card card--front">
    <div class="portrait" role="img" aria-label="Portrait photo of the financial advisor"></div>
    <div class="contact">
      <p class="contact__name">DALE KORVANEK | FINANCIAL ADVISOR</p>
      <div class="contact__rule"></div>
      <p class="contact__line">58271 Marbleton Creek Rd., #340 St. Louis, MO 63907</p>
      <p class="contact__line"><span class="label">M:</span> (314) 555-0182 | <span class="label">C:</span> (314) 555-0927| <span class="label">F:</span> (314) 555-0346</p>
      <p class="contact__line"><span class="label">E:</span> daleK@qrvlx.com</p>
    </div>
  </section>

  <section class="card card--back">
    <div class="services-tab">
      <p>LIFE INSURANCE</p>
      <p>RETIREMENT</p>
      <p>EMPLOYEE BENEFITS</p>
    </div>
    <div class="disclaimer">
      <p>Securities offered through the B.W. Harbor Trading Company</p>
      <p>Member NARCU/TLOB</p>
      <p>Four Quarry Plaza, Cincinnati, Ohio 45917</p>
      <p>513-555-0263</p>
      <p>Investment Advisory Services offered through B.W. Holdings Management Company.</p>
    </div>
  </section>
</body>
</html>
```